Artwork-Design (Cover) für Musikalbum
Zielgruppe
Wir sind eine Tonträgerfirma und bewegen uns im Low-Budget-Segment.
Aufgabenstellung
Artwork-Design (Cover) für ein Musikalbum : 'Große Momente im Reich klassischer Ouvertüren'
Wir benötigen nicht das komplette Artwork, sondern ein Frontcover
(121 x 120 mm + 20 mm Beschnitt) wg. etwaiger Verschiebung der Positionierung.
Fertigstellung (Aufziehen des Inlays und Labels) erfolgt später bei uns im Hause.
Wir benötigen später eine offene psd-Datei mit allen Ebenen.
Wichtig: Schriften nicht gerastert ggfs. Schrift mitliefern.
Was wir uns vorstellen:
- Entsprechend der Musik Bild,
- Bildmaterial sollte bei pixoranta, bildavero oder q-frame ausgesucht werden, das Bildmaterial wird dann später auch von uns dort eingekauft.
- keine Künstlerfotos.
Wir freuen uns und sind sehr gespannt auf eure Vorschläge,
bei Fragen gerne mailen

```html
<!DOCTYPE html>
<html lang="de">
<head>
<meta charset="utf-8">
<title>Große Momente im Reich klassischer Ouvertüren – Frontcover</title>
<link rel="stylesheet" href="https://fonts.googleapis.com/css2?family=Lato:wght@700&family=Mrs+Saint+Delafield&display=swap">
<style>
  :root {
    --mat: #060609;
    --paper: #f1ede5;
    --paper-shade: #e9e2d8;
    --wine: #6b1620;
    --script: #9a3a43;
    --wash-deep: #c4555a;
    --wash-mid: #dc8f86;
    --wash-soft: #efc9bd;
  }
  * { margin: 0; padding: 0; box-sizing: border-box; }
  html, body {
    width: 1200px;
    height: 1192px;
    overflow: hidden;
    background: var(--mat);
  }
  .cover {
    position: absolute;
    left: 150px;
    top: 150px;
    width: 902px;
    height: 892px;
    overflow: hidden;
    background: radial-gradient(ellipse at 50% 40%, var(--paper) 0%, var(--paper) 60%, var(--paper-shade) 100%);
  }
  .cover__artwork {
    position: absolute;
    left: 40px;
    top: 80px;
    width: 820px;
    height: 760px;
    background:
      radial-gradient(ellipse 46% 22% at 55% 62%, var(--wash-deep) 0%, rgba(196,85,90,0.55) 55%, rgba(196,85,90,0) 100%),
      radial-gradient(ellipse 52% 44% at 50% 52%, var(--wash-mid) 0%, rgba(220,143,134,0.6) 45%, rgba(239,201,189,0.35) 75%, rgba(239,201,189,0) 100%);
    transform: rotate(-18deg);
  }
  .cover__kicker {
    position: absolute;
    left: 93px;
    top: 124px;
    font-family: "Lato", "Helvetica Neue", sans-serif;
    font-weight: 700;
    font-size: 27px;
    line-height: 37px;
    letter-spacing: -0.3px;
    color: var(--wine);
    text-transform: uppercase;
  }
  .cover__title {
    position: absolute;
    left: 40px;
    top: 280px;
    width: 860px;
    text-align: center;
    font-family: "Mrs Saint Delafield", "Brush Script MT", cursive;
    font-weight: 400;
    font-size: 215px;
    line-height: 1;
    color: var(--script);
    transform: rotate(-18deg);
    transform-origin: 50% 50%;
    white-space: nowrap;
  }
</style>
</head>
<body>
  <main class="cover">
    <div class="cover__artwork" role="img" aria-label="Aquarellierte Geige in Rot- und Rosétönen mit Farbspritzern, schräg über das Cover gelegt"></div>
    <p class="cover__kicker">Große Momente<br>im Reich<br>klassischer</p>
    <h1 class="cover__title">Ouvertüren</h1>
  </main>
</body>
</html>
```